Band Needs Quick Turnaround on CD Cover Text Placement

We have a great image for our cover. We need an expert at making the band name and title look fantastic. Please submit your ideas asap as we are on a time crunch to launch a crowd funding campaign. All we need is the cover design for now.

Target Market(s)

music fans who love rock, classic rock, americana, roots rock

Industry/Entity Type

Music Download

Font styles to use
Sans Serif

Colors
ffffff

Requirements
Must have
• The Band Name:
• Ray Calloway & Moss Harbor Drifters
• (text should all be the same size) should be near the top right side of the design.
• The Album title:
• Past the Quiet Road
• Text Color: White or something close to white.
Should not have
• Other images or other font colors

```html
<!DOCTYPE html>
<html lang="en">
<head>
<meta charset="utf-8">
<title>Past the Quiet Road — Ray Calloway &amp; Moss Harbor Drifters</title>
<link rel="stylesheet" href="https://fonts.googleapis.com/css2?family=Anton&family=Roboto:wght@400;700&display=swap">
<style>
  :root {
    --ink: #0b0b0b;
    --paper: #f4f4f4;
    --photo-dark: #0e0e0e;
    --photo-mid: #333333;
    --photo-light: #4e4e4e;
  }
  * { margin: 0; padding: 0; box-sizing: border-box; }
  html, body {
    width: 1200px;
    height: 1200px;
    overflow: hidden;
    background: var(--ink);
  }
  .cover {
    position: relative;
    width: 1200px;
    height: 1200px;
    overflow: hidden;
    background: var(--ink);
  }
  .cover-photo {
    position: absolute;
    inset: 0;
    background:
      radial-gradient(ellipse 42% 55% at 80% 55%, var(--photo-light) 0%, var(--photo-mid) 40%, transparent 78%),
      radial-gradient(ellipse 40% 45% at 45% 30%, #262626 0%, transparent 70%),
      linear-gradient(90deg, var(--photo-dark) 0%, #181818 35%, #222222 60%, #1a1a1a 100%);
  }

  .album-title {
    position: absolute;
    inset: 0;
    font-family: "Anton", "Oswald", sans-serif;
    font-weight: 400;
    text-transform: uppercase;
  }
  .title-line {
    position: absolute;
    display: block;
    line-height: 1;
    letter-spacing: -1px;
    white-space: nowrap;
  }
  .title-line--boxed {
    background: var(--paper);
    color: var(--ink);
    overflow: hidden;
  }
  .title-line--open { color: var(--paper); }

  .title-line--past {
    left: 0; top: 169px; width: 460px; height: 283px;
    font-size: 243px; padding: 27px 0 0 42px;
  }
  .title-line--the {
    left: 60px; top: 452px;
    font-size: 205px;
  }
  .title-line--quiet {
    left: 0; top: 645px; width: 530px; height: 270px;
    font-size: 255px; padding: 12px 0 0 42px;
  }
  .title-line--road {
    left: 80px; top: 923px;
    font-size: 245px;
  }

  .band-name {
    position: absolute;
    right: 40px;
    top: 50px;
    font-family: "Roboto", "Helvetica Neue", sans-serif;
    font-weight: 400;
    font-size: 32px;
    line-height: 52px;
    letter-spacing: 2px;
    color: var(--paper);
    text-align: right;
    text-transform: uppercase;
  }
  .band-name strong { font-weight: 700; }
  .band-name__join { text-transform: none; }
</style>
</head>
<body>
  <main class="cover">
    <div class="cover-photo" role="img" aria-label="Black and white close-up photograph of an elephant's head filling the cover"></div>

    <h1 class="album-title">
      <span class="title-line title-line--boxed title-line--past">Past</span>
      <span class="title-line title-line--open title-line--the">The</span>
      <span class="title-line title-line--boxed title-line--quiet">Quiet</span>
      <span class="title-line title-line--open title-line--road">Road</span>
    </h1>

    <p class="band-name">
      <strong>Ray</strong> Calloway<br>
      <span class="band-name__join">and</span><br>
      <strong>Moss Harbor</strong> Drifters
    </p>
  </main>
</body>
</html>
```